Mobile Game / Web Game Site
Modern, simple, fun, appealing
Games
We are a game design shop, headed by a 30 year veteran of the video game industry. We provide our games to player for free and also allow players to compete against each other.
We really like a clear direction, a purpose that is obvious. But we also like giving the player and customers plenty of depth when they desire. We are the oldest, longest running skill game on the net. We create our own games for a unique atmosphere, and need our site to reflect this same amount of creativity and professionalism.
top
http://www.vornaleaf.example/tunebox/
http://www.qrt-studioworks.example/
http://www.playvexor.example/
We also like the use of rich wood textures, metals, ivory texture, mother of pearl, etc in our games. It may work for the site as well if used sparingly. Thank you for reading!
this was my initial attempt. It displays the different elements needed
I really like the feel of this
nice clean retro feel

```html
<!DOCTYPE html>
<html lang="en">
<head>
<meta charset="utf-8">
<title>Game Site Home</title>
<link href="https://fonts.googleapis.com/css2?family=Open+Sans:wght@300;400;600&family=Oswald:wght@400&display=swap" rel="stylesheet">
<style>
:root{
  --wood-dark:#6e3a12;
  --wood-mid:#a4581c;
  --wood-light:#c77a35;
  --panel:#f4f4f4;
  --panel-edge:#d6d6d6;
  --bar-dark:#2e2e2e;
  --bar-mid:#4a4a4a;
  --text:#333333;
  --text-light:#ffffff;
  --muted:#666666;
  --felt-dark:#0f4a1a;
  --felt-light:#2a7a33;
  --accent:#f2a41a;
  --icon-edge:#d98a6a;
}
*{box-sizing:border-box;margin:0;padding:0}
html,body{width:1200px;height:1091px;overflow:hidden}
body{
  position:relative;
  font-family:"Open Sans",Arial,sans-serif;
  color:var(--text);
  background:
    repeating-linear-gradient(90deg,rgba(0,0,0,.06) 0 6px,rgba(255,255,255,.03) 6px 14px,rgba(0,0,0,.04) 14px 31px),
    radial-gradient(ellipse at 50% 40%,var(--wood-light) 0%,var(--wood-mid) 45%,var(--wood-dark) 100%);
}
.abs{position:absolute}
.brand{left:168px;top:22px;font-size:66px;font-weight:300;color:var(--text-light);letter-spacing:3px}
.main-nav{left:124px;top:130px;width:624px;height:48px;background:linear-gradient(var(--bar-mid),var(--bar-dark));border-radius:4px;box-shadow:0 2px 4px rgba(0,0,0,.4)}
.main-nav a{position:absolute;top:12px;font-size:19px;color:var(--text-light);text-decoration:none}
.search{left:769px;top:130px;width:307px;height:48px;background:linear-gradient(var(--bar-mid),var(--bar-dark));border-radius:4px;box-shadow:0 2px 4px rgba(0,0,0,.4)}
.search .field{position:absolute;left:14px;top:12px;width:222px;height:24px;background:#fff;border-radius:12px;font-size:13px;padding:3px 12px;color:var(--muted)}
.search .go{position:absolute;left:245px;top:12px;width:50px;height:24px;background:linear-gradient(#fff,#ddd);border-radius:12px;font-size:13px;text-align:center;line-height:24px}
.label{font-size:19px;color:var(--text-light);text-transform:uppercase;letter-spacing:.5px}
.panel{background:var(--panel);border:2px solid var(--panel-edge);border-radius:6px;box-shadow:0 2px 6px rgba(0,0,0,.35)}
.banner{left:136px;top:248px;width:603px;height:240px;background:radial-gradient(ellipse at 35% 45%,var(--felt-light),var(--felt-dark));border-radius:3px}
.banner-title{position:absolute;left:302px;top:104px;font-family:"Oswald",Arial,sans-serif;font-size:38px;line-height:46px;white-space:nowrap;color:var(--text-light)}
.dot{width:22px;height:22px;border-radius:50%;border:2px solid #bbb;background:#fff}
.dot.active{background:var(--accent);border-color:#d98d0e}
.tab{top:248px;width:86px;height:24px;background:linear-gradient(#fff,#e2e2e2);border:1px solid #bbb;border-radius:4px;font-size:13px;text-align:center;line-height:22px}
.thumb{width:98px;height:74px;background:#fff;border:1px solid #ccc;border-radius:3px}
.tour-name{font-size:27px;width:180px;text-align:center;color:var(--text)}
.head{font-size:18px;text-transform:uppercase;color:var(--text)}
.divider{width:2px;background:#ddd}
.video{left:130px;top:585px;width:299px;height:178px;background:linear-gradient(135deg,#cfcfcf,#8c8c8c 55%,#5a5a5a);border-radius:2px}
.btn{height:24px;background:linear-gradient(#fff,#e0e0e0);border:1px solid #bbb;border-radius:12px;font-size:12px;text-align:center;line-height:22px}
.card-icon{width:44px;height:54px;background:#fff;border:2px solid var(--icon-edge);border-radius:3px;display:flex;align-items:center;justify-content:center}
.img-cell{width:46px;height:50px}
.event-name{font-size:14px}
.small{font-size:13px;line-height:19px}
.input{height:22px;border:1px solid #bbb;border-radius:3px;background:#fff;font-size:13px;padding:1px 14px}
.social-sq{width:24px;height:24px;border-radius:3px}
.footer{left:0;width:1200px;top:1024px;text-align:center;font-size:12px;color:rgba(255,255,255,.8)}
</style>
</head>
<body>
<svg width="0" height="0" style="position:absolute">
  <symbol id="spade" viewBox="0 0 24 26">
    <path d="M12 1C8 7 2 10 2 15a5 5 0 0 0 8.5 3.5L9 25h6l-1.5-6.5A5 5 0 0 0 22 15c0-5-6-8-10-14z" fill="#000"/>
  </symbol>
</svg>

<div class="abs brand">LOGO</div>

<nav class="abs main-nav">
  <a style="left:24px">HOME</a>
  <a style="left:133px">SUPPORT</a>
  <a style="left:275px">COMMUNITY</a>
  <a style="left:458px">FREE GAMES</a>
</nav>
<div class="abs search"><div class="field">search...</div><div class="go">GO</div></div>

<div class="abs label" style="left:139px;top:202px">Popular Games</div>
<div class="abs label" style="left:783px;top:202px">Tournaments</div>

<section class="abs panel" style="left:124px;top:234px;width:627px;height:292px"></section>
<div class="abs banner" role="img" aria-label="Playing cards on green felt promoting new games"><div class="banner-title">NEW GAMES 2012</div></div>
<div class="abs dot active" style="left:477px;top:497px"></div>
<div class="abs dot" style="left:512px;top:497px"></div>
<div class="abs dot" style="left:548px;top:497px"></div>

<section class="abs panel" style="left:774px;top:234px;width:302px;height:292px"></section>
<div class="abs tab" style="left:785px">Option 1</div>
<div class="abs tab" style="left:883px">Option 1</div>
<div class="abs tab" style="left:980px">Option 1</div>
<div class="abs thumb" style="left:783px;top:281px"></div>
<div class="abs thumb" style="left:783px;top:364px"></div>
<div class="abs thumb" style="left:783px;top:446px"></div>
<div class="abs tour-name" style="left:886px;top:300px">SOLITAIRE</div>
<div class="abs tour-name" style="left:886px;top:383px">MEGASTARS</div>
<div class="abs tour-name" style="left:886px;top:465px">MAKE 13</div>

<section class="abs panel" style="left:124px;top:541px;width:952px;height:284px"></section>
<div class="abs divider" style="left:440px;top:548px;height:270px"></div>
<div class="abs divider" style="left:763px;top:548px;height:270px"></div>
<div class="abs head" style="left:133px;top:546px">Videos</div>
<div class="abs head" style="left:458px;top:546px">Events</div>
<div class="abs head" style="left:777px;top:546px">Images</div>

<div class="abs video" role="img" aria-label="Video still of a hand of playing cards">
  <svg class="abs" style="left:120px;top:60px" width="60" height="60" viewBox="0 0 60 60"><circle cx="30" cy="30" r="28" fill="rgba(40,40,40,.75)" stroke="#fff" stroke-width="2"/><path d="M23 17l20 13-20 13z" fill="#fff"/></svg>
</div>
<div class="abs btn" style="left:340px;top:793px;width:80px">show all</div>

<div class="abs card-icon" style="left:464px;top:591px"><svg width="22" height="24"><use href="#spade"/></svg></div>
<div class="abs card-icon" style="left:464px;top:663px"><svg width="22" height="24"><use href="#spade"/></svg></div>
<div class="abs card-icon" style="left:464px;top:735px"><svg width="22" height="24"><use href="#spade"/></svg></div>
<div class="abs event-name" style="left:520px;top:608px">Solitaire Multiplayer</div>
<div class="abs event-name" style="left:520px;top:680px">Solitaire Multiplayer</div>
<div class="abs event-name" style="left:520px;top:752px">Solitaire Multiplayer</div>
<div class="abs btn" style="left:680px;top:607px;width:59px">join</div>
<div class="abs btn" style="left:680px;top:679px;width:59px">join</div>
<div class="abs btn" style="left:680px;top:751px;width:59px">join</div>
<div class="abs btn" style="left:660px;top:793px;width:80px">show all</div>

<div class="abs" style="left:777px;top:591px;width:290px;display:grid;grid-template-columns:repeat(5,46px);column-gap:13px;row-gap:16px">
  <div class="card-icon img-cell"><svg width="22" height="24"><use href="#spade"/></svg></div>
  <div class="card-icon img-cell"><svg width="22" height="24"><use href="#spade"/></svg></div>
  <div class="card-icon img-cell"><svg width="22" height="24"><use href="#spade"/></svg></div>
  <div class="card-icon img-cell"><svg width="22" height="24"><use href="#spade"/></svg></div>
  <div class="card-icon img-cell"><svg width="22" height="24"><use href="#spade"/></svg></div>
  <div class="card-icon img-cell"><svg width="22" height="24"><use href="#spade"/></svg></div>
  <div class="card-icon img-cell"><svg width="22" height="24"><use href="#spade"/></svg></div>
  <div class="card-icon img-cell"><svg width="22" height="24"><use href="#spade"/></svg></div>
  <div class="card-icon img-cell"><svg width="22" height="24"><use href="#spade"/></svg></div>
  <div class="card-icon img-cell"><svg width="22" height="24"><use href="#spade"/></svg></div>
  <div class="card-icon img-cell"><svg width="22" height="24"><use href="#spade"/></svg></div>
  <div class="card-icon img-cell"><svg width="22" height="24"><use href="#spade"/></svg></div>
  <div class="card-icon img-cell"><svg width="22" height="24"><use href="#spade"/></svg></div>
  <div class="card-icon img-cell"><svg width="22" height="24"><use href="#spade"/></svg></div>
  <div class="card-icon img-cell"><svg width="22" height="24"><use href="#spade"/></svg></div>
</div>
<div class="abs btn" style="left:982px;top:793px;width:80px">show all</div>

<section class="abs panel" style="left:124px;top:837px;width:305px;height:168px"></section>
<div class="abs divider" style="left:130px;top:882px;width:292px;height:2px"></div>
<div class="abs head" style="left:146px;top:842px">Contact Us</div>
<div class="abs small" style="left:148px;top:908px">Email: info@pebblequestplay.example<br>Address: Pebble Lane 123, TA<br>Phone: 800-555-0147</div>

<section class="abs panel" style="left:443px;top:837px;width:311px;height:168px"></section>
<div class="abs divider" style="left:450px;top:882px;width:298px;height:2px"></div>
<div class="abs head" style="left:464px;top:842px">Newsletter</div>
<div class="abs input" style="left:470px;top:887px;width:240px">Name</div>
<div class="abs input" style="left:470px;top:917px;width:240px">E-mail</div>
<div class="abs btn" style="left:621px;top:947px;width:89px">subscribe</div>

<section class="abs panel" style="left:774px;top:837px;width:302px;height:168px"></section>
<div class="abs divider" style="left:781px;top:882px;width:288px;height:2px"></div>
<div class="abs head" style="left:790px;top:842px">Social Community</div>
<div class="abs small" style="left:790px;top:893px">Follow us on:</div>
<div class="abs social-sq" style="left:790px;top:914px;background:#3b5b98"></div>
<div class="abs social-sq" style="left:820px;top:914px;background:#3fa9e0"></div>
<div class="abs social-sq" style="left:850px;top:914px;background:#f08a24"></div>

<div class="abs footer">All rights reserved pebblequestplay 2012</div>
</body>
</html>
```